Upscale business cards needed for family business

We need professional business cards created for several family members. We are a family business holding company. We would like these relatively simple and straightforward, but also with a unique element to set them apart. Probably stick with neutral and simple colors - white, grey etc. We need space for the traditional elements, including name, title, address, email/phone number. And we will be creating several from this template so it needs to be template that is easy to switch information in and out of.

Industry/Entity Type

Business

Contact Information for Business Card

Please include the attached Dunmore Ventures logo.

Requirements
Must have
• The attached Dunmore Ventures logo.

```html
<!DOCTYPE html>
<html lang="en">
<head>
<meta charset="utf-8">
<title>Dunmore Ventures – Business Card</title>
<link rel="stylesheet" href="https://fonts.googleapis.com/css2?family=Libre+Franklin:wght@400;500;700&display=swap">
<style>
  :root {
    --card-white: #ffffff;
    --ink: #111111;
    --ink-soft: #4d4d4d;
    --brand-ink: #2b2b2b;
    --grey-light: #c9c9c9;
    --grey-edge: #b4b4b4;
    --grey-band: #a0a0a0;
    --grey-faint: #f1f1f1;
    --grey-fainter: #f7f7f7;
    --rule-grey: #a8a8a8;
    --icon-box: #595959;
    --icon-shadow: #8c8c8c;
    --gold-light: #efe3c4;
    --gold-deep: #d4a020;
  }
  html, body {
    margin: 0;
    padding: 0;
    width: 1200px;
    height: 734px;
    overflow: hidden;
    background: var(--card-white);
  }
  .card {
    position: relative;
    width: 1200px;
    height: 734px;
    overflow: hidden;
    background: var(--card-white);
    font-family: "Libre Franklin", Arial, sans-serif;
  }
  .card-backdrop {
    position: absolute;
    inset: 0;
    width: 1200px;
    height: 734px;
  }
  .brand-name {
    position: absolute;
    left: 0;
    width: 1200px;
    padding-left: 244px;
    box-sizing: border-box;
    top: 140px;
    text-align: center;
    font-size: 42px;
    font-weight: 500;
    letter-spacing: 3px;
    color: var(--brand-ink);
    margin: 0;
  }
  .rule {
    position: absolute;
    right: 0;
    height: 0;
  }
  .rule--grey { top: 242px; left: 240px; border-top: 4px solid var(--rule-grey); }
  .rule--top { top: 250px; left: 240px; border-top: 3px solid var(--ink); }
  .rule--bottom { top: 360px; left: 291px; border-top: 3px solid var(--ink); }
  .person {
    position: absolute;
    left: 528px;
    width: 400px;
    text-align: center;
    margin: 0;
  }
  .person-name {
    top: 268px;
    font-size: 33px;
    font-weight: 700;
    color: var(--ink);
    letter-spacing: 1px;
  }
  .person-title {
    top: 316px;
    font-size: 25px;
    font-weight: 700;
    color: var(--ink-soft);
    letter-spacing: 1px;
  }
  .contact-list {
    list-style: none;
    margin: 0;
    padding: 0;
  }
  .contact-icon {
    position: absolute;
    width: 68px;
    height: 51px;
    background: var(--icon-box);
    box-shadow: 9px 6px 0 var(--icon-shadow);
    display: flex;
    align-items: center;
    justify-content: center;
  }
  .contact-icon svg { width: 30px; height: 30px; fill: #ffffff; }
  .contact-text {
    position: absolute;
    font-size: 25px;
    color: var(--ink);
    white-space: nowrap;
    line-height: 1;
  }
  .contact--phone .contact-icon { left: 221px; top: 430px; }
  .contact--phone .contact-text { left: 387px; top: 437px; }
  .contact--email .contact-icon { left: 252px; top: 495px; }
  .contact--email .contact-text { left: 421px; top: 502px; }
  .contact--web .contact-icon { left: 286px; top: 560px; }
  .contact--web .contact-text { left: 474px; top: 567px; }
  .contact--address .contact-icon { left: 340px; top: 622px; }
  .contact--address .contact-text { left: 551px; top: 634px; }
</style>
</head>
<body>
<div class="card">
  <svg class="card-backdrop" viewBox="0 0 1063 650" preserveAspectRatio="none" aria-hidden="true">
    <defs>
      <linearGradient id="gold-sweep" x1="0" y1="0" x2="0" y2="1">
        <stop offset="0" stop-color="var(--gold-light)"/>
        <stop offset="0.5" stop-color="#ddb860"/>
        <stop offset="1" stop-color="var(--gold-deep)"/>
      </linearGradient>
    </defs>
    <path d="M1063,90 Q860,380 740,650 L1063,650 Z" fill="var(--grey-fainter)"/>
    <path d="M1063,200 Q900,430 790,650 L1063,650 Z" fill="var(--grey-faint)"/>
    <path d="M150,0 Q245,440 610,650 L0,650 L0,0 Z" fill="var(--grey-band)"/>
    <path d="M150,0 Q215,430 535,650 L0,650 L0,0 Z" fill="url(#gold-sweep)"/>
    <path d="M146,0 Q195,420 505,650 L0,650 L0,0 Z" fill="var(--grey-band)"/>
    <path d="M142,0 Q180,410 470,650 L0,650 L0,0 Z" fill="var(--grey-light)"/>
    <path d="M0,0 L18,0 Q60,420 245,650 L0,650 Z" fill="var(--grey-edge)"/>
  </svg>

  <p class="brand-name">DUNMORE VENTURES INC</p>

  <div class="rule rule--grey"></div>
  <div class="rule rule--top"></div>
  <h1 class="person person-name">NAME</h1>
  <p class="person person-title">TITTLE GOES HERE</p>
  <div class="rule rule--bottom"></div>

  <ul class="contact-list">
    <li class="contact contact--phone">
      <span class="contact-icon"><svg viewBox="0 0 24 24"><path d="M6.6 10.8c1.4 2.8 3.8 5.1 6.6 6.6l2.2-2.2c.3-.3.7-.4 1-.2 1.1.4 2.3.6 3.6.6.6 0 1 .4 1 1V20c0 .6-.4 1-1 1C10.6 21 3 13.4 3 4c0-.6.4-1 1-1h3.5c.6 0 1 .4 1 1 0 1.3.2 2.5.6 3.6.1.3 0 .7-.2 1z"/></svg></span>
      <span class="contact-text">Phone number goes here</span>
    </li>
    <li class="contact contact--email">
      <span class="contact-icon"><svg viewBox="0 0 24 24"><path d="M2 5h20v14H2z M3.5 6.5 12 13l8.5-6.5" fill="#ffffff" stroke="#595959" stroke-width="1.4"/></svg></span>
      <span class="contact-text">Email goes here</span>
    </li>
    <li class="contact contact--web">
      <span class="contact-icon"><svg viewBox="0 0 24 24" fill="none" stroke="#ffffff" stroke-width="1.5" style="fill:none"><circle cx="12" cy="12" r="9.5"/><ellipse cx="12" cy="12" rx="4.5" ry="9.5"/><path d="M2.5 12h19M4 7h16M4 17h16M12 2.5v19"/></svg></span>
      <span class="contact-text">Web adress goes here</span>
    </li>
    <li class="contact contact--address">
      <span class="contact-icon"><svg viewBox="0 0 24 24"><path d="M12 2a7 7 0 0 0-7 7c0 5 7 13 7 13s7-8 7-13a7 7 0 0 0-7-7zm0 9.5A2.5 2.5 0 1 1 12 6.5a2.5 2.5 0 0 1 0 5z"/></svg></span>
      <span class="contact-text">Adress goes here</span>
    </li>
  </ul>
</div>
</body>
</html>
```